New Signage Design Project

Real estate company looking for signage, PowerPoint and stationery branding. Signs will be placed in front of homes and other properties being sold

Name of company is Birch Crest, LLC

Requirements
Must have
• Name of company - Birch Crest, LLC

```html
<!DOCTYPE html>
<html lang="en">
<head>
<meta charset="utf-8">
<title>Birch Crest, LLC – For Sale Sign</title>
<link rel="stylesheet" href="https://fonts.googleapis.com/css2?family=Arimo:wght@400;700&family=Noto+Sans:wght@700;800&display=swap">
<style>
  :root {
    --sign-white: #ffffff;
    --sign-charcoal: #343434;
    --brand-red: #b11f24;
    --phone-blue: #0620a9;
  }
  html, body {
    margin: 0;
    padding: 0;
    width: 1200px;
    height: 900px;
    overflow: hidden;
    background: var(--sign-white);
  }
  .sign {
    display: block;
    width: 1200px;
    height: 900px;
  }
  .sign__band { fill: var(--sign-charcoal); }
  .sign__strip { fill: var(--sign-white); }
  .badge__gap { fill: var(--sign-white); }
  .badge__ring { fill: var(--sign-charcoal); }
  .badge__face { fill: var(--sign-white); }
  .badge__name {
    font-family: "Arimo", Arial, sans-serif;
    font-weight: 700;
    font-size: 34px;
    fill: var(--sign-charcoal);
  }
  .strip-phone {
    font-family: "Noto Sans", Verdana, sans-serif;
    font-weight: 800;
    font-size: 64px;
    fill: var(--sign-charcoal);
  }
  .strip-phone__accent { fill: var(--phone-blue); }
  .headline {
    font-family: "Arimo", Arial, sans-serif;
    font-weight: 700;
    font-size: 142px;
    fill: var(--brand-red);
  }
  .footer-phone {
    font-family: "Noto Sans", Verdana, sans-serif;
    font-weight: 800;
    font-size: 52px;
    fill: var(--phone-blue);
  }
</style>
</head>
<body>
<svg class="sign" viewBox="0 0 1200 900" xmlns="http://www.w3.org/2000/svg" aria-label="Birch Crest, LLC for sale sign">
  <rect class="sign__band" x="0" y="40" width="1200" height="627"/>
  <rect class="sign__strip" x="440" y="292" width="760" height="116"/>

  <g class="badge">
    <circle class="badge__gap" cx="197" cy="360" r="280"/>
    <circle class="badge__ring" cx="197" cy="360" r="266"/>
    <circle class="badge__face" cx="197" cy="360" r="227"/>
    <text class="badge__name" x="197" y="372" text-anchor="middle">BIRCH CREST, LLC</text>
  </g>

  <text class="strip-phone" x="500" y="371" textLength="662" lengthAdjust="spacingAndGlyphs">1-855-BIRCH CRES<tspan class="strip-phone__accent">T</tspan></text>

  <text class="headline" x="194" y="797" textLength="813" lengthAdjust="spacing">FOR SALE</text>

  <text class="footer-phone" x="317" y="858" textLength="565" lengthAdjust="spacing">1-855-555-0142</text>
</svg>
</body>
</html>
```